SUMMIT PAVING & EARTHWORKS

I would like the front of the card to have my logo centred.
I need it to have my contact details on the back of the card which are: SummitPavingEarthworks@brindlemail.com
0413862574
and a Facebook icon

```html
<!DOCTYPE html>
<html lang="en">
<head>
<meta charset="utf-8">
<title>Summit Paving &amp; Earthworks — Business Card</title>
<link rel="stylesheet" href="https://fonts.googleapis.com/css2?family=Saira+Condensed:wght@700&family=Poppins:wght@400&display=swap">
<style>
  :root {
    --backdrop: #b3b3b3;
    --card-black: #020202;
    --pattern-light: #1a1a1a;
    --pattern-mid: #0c0c0c;
    --brand-blue: #1f7fd0;
    --text-white: #f4f4f4;
    --icon-white: #e6e6e6;
  }
  * { box-sizing: border-box; margin: 0; padding: 0; }
  html, body {
    width: 1200px;
    height: 1200px;
    overflow: hidden;
    background: var(--backdrop);
  }
  .canvas {
    position: relative;
    width: 1200px;
    height: 1200px;
  }
  .card {
    position: absolute;
    left: 223px;
    width: 755px;
    height: 431px;
    background: var(--card-black);
    overflow: hidden;
  }
  .card--front { top: 114px; }
  .card--back { top: 655px; }

  .card__pattern {
    position: absolute;
    inset: 0;
    background:
      radial-gradient(ellipse 70% 80% at 50% 45%, var(--pattern-light) 0%, var(--pattern-mid) 55%, var(--card-black) 100%);
  }

  .wordmark {
    position: absolute;
    font-family: "Saira Condensed", "Arial Narrow", sans-serif;
    font-weight: 700;
    color: var(--brand-blue);
    text-transform: uppercase;
    text-align: center;
  }
  .wordmark--front {
    left: 0;
    right: 0;
    top: 160px;
    font-size: 54px;
    line-height: 52px;
    letter-spacing: 1px;
  }
  .wordmark--back {
    left: 88px;
    top: 150px;
    width: 152px;
    font-size: 31px;
    line-height: 32px;
    letter-spacing: 0.5px;
  }

  .contact-list {
    position: absolute;
    left: 274px;
    top: 165px;
    list-style: none;
    font-family: "Poppins", Arial, sans-serif;
    font-weight: 400;
    font-size: 16.5px;
    color: var(--text-white);
  }
  .contact-list__item {
    display: flex;
    align-items: center;
    height: 22px;
    margin-bottom: 14px;
  }
  .contact-list__icon {
    width: 15px;
    height: 15px;
    margin-right: 14px;
    flex-shrink: 0;
  }
  .contact-list__rule {
    width: 132px;
    height: 2px;
    background: linear-gradient(90deg, var(--text-white) 60%, rgba(255,255,255,0.2));
    border-radius: 1px;
  }
</style>
</head>
<body>
<main class="canvas">

  <section class="card card--front" aria-label="Card front">
    <div class="card__pattern" role="img" aria-label="Dark geometric star pattern background"></div>
    <h1 class="wordmark wordmark--front">Summit Paving<br>&amp; Earthworks</h1>
  </section>

  <section class="card card--back" aria-label="Card back">
    <div class="card__pattern" role="img" aria-label="Dark geometric star pattern background"></div>
    <p class="wordmark wordmark--back">Summit<br>Paving &amp;<br>Earthworks</p>

    <ul class="contact-list">
      <li class="contact-list__item">
        <svg class="contact-list__icon" viewBox="0 0 16 16" aria-hidden="true">
          <circle cx="8" cy="8" r="7" fill="none" stroke="var(--icon-white)" stroke-width="1.1"/>
          <path d="M5.4 4.6c.4-.3.8-.3 1 .1l.7 1.2c.2.3.1.6-.2.8l-.4.3c.4.9 1.1 1.6 2 2l.3-.4c.2-.3.5-.4.8-.2l1.2.7c.4.2.4.6.1 1-.6.7-1.3.9-2.1.6-1.8-.7-3.2-2.1-3.9-3.9-.3-.8-.1-1.6.5-2.2z" fill="var(--icon-white)"/>
        </svg>
        <span>0413862574</span>
      </li>
      <li class="contact-list__item">
        <svg class="contact-list__icon" viewBox="0 0 16 16" aria-hidden="true">
          <circle cx="8" cy="8" r="7" fill="none" stroke="var(--icon-white)" stroke-width="1.1"/>
          <rect x="4.4" y="5.4" width="7.2" height="5.2" rx="0.6" fill="var(--icon-white)"/>
          <path d="M4.6 5.7 8 8.4l3.4-2.7" fill="none" stroke="var(--card-black)" stroke-width="0.9"/>
        </svg>
        <span>SummitPavingEarthworks@brindlemail.com</span>
      </li>
      <li class="contact-list__item">
        <svg class="contact-list__icon" viewBox="0 0 16 16" aria-hidden="true">
          <circle cx="8" cy="8" r="7.2" fill="var(--icon-white)"/>
        </svg>
        <span class="contact-list__rule" role="img" aria-label="Social page"></span>
      </li>
    </ul>
  </section>

</main>
</body>
</html>
```